Modern Quillby Tree Care Website

I need a website for a full service Tree Care company. The company provides tree pruning, tree removal, tree preservation, emergency services, stump grinding, and emergency tree services.

Target Market(s)

Customers that need tree services

Industry/Entity Type

Landscaping, Tree Services

Coding

Coded - Design and coding required

Number of Pages Required

5+ page

Font styles to use
Sans Serif

Requirements
Must have
• Good clean design that showcases the services the company provides.
Nice to have
• Services page; contact form, blog, home page, about page

```html
<!DOCTYPE html>
<html lang="en">
<head>
<meta charset="utf-8">
<title>Quillby Tree Care – Website Pages</title>
<link rel="stylesheet" href="https://fonts.googleapis.com/css2?family=Ubuntu:wght@400;500;700&display=swap">
<style>
:root{
  --leaf:#6f9b2c;
  --leaf-soft:#eef3e5;
  --forest:#27321b;
  --forest-line:#3a4729;
  --ink:#2e3328;
  --mute:#8b8f87;
  --mist:#e7e9ea;
  --paper:#ffffff;
  --photo-deep:#1f2818;
  --photo-mid:#3f4d2c;
  --photo-light:#6c7f45;
}
html,body{margin:0;width:1200px;height:675px;overflow:hidden;background:var(--paper)}
body{position:relative;font-family:'Ubuntu',sans-serif;color:var(--ink)}
p,h1,h2,h3,h4,ul{margin:0;padding:0}
ul{list-style:none}

/* page frames */
.page{position:absolute;width:600px;transform-origin:0 0;background:var(--paper);overflow:hidden}
.page--home{left:46px;top:28px;height:1860px;transform:scale(.337)}
.page--services{left:278px;top:67px;height:1164px;transform:scale(.468)}
.page--about{left:589px;top:67px;height:1268px;transform:scale(.43)}
.page--gallery{left:873px;top:28px;height:734px;transform:scale(.527)}
.page--contact{left:918px;top:426px;height:759px;transform:scale(.377)}

/* navigation */
.nav{position:absolute;top:12px;left:40px;right:40px;height:22px;display:flex;align-items:center;z-index:2;font-size:6.5px;color:#fff}
.brand{display:flex;align-items:center;gap:4px;font-weight:700;font-size:6.5px;text-transform:uppercase;margin-right:auto;color:#fff}
.brand-mark{width:12px;height:12px;background:var(--leaf);display:block}
.nav-links{display:flex;gap:13px;margin-right:14px}
.nav-cta{border:1px solid #fff;border-radius:10px;padding:3px 9px}

/* banners */
.hero,.banner{position:relative;overflow:hidden;color:#fff}
.hero{height:300px;border-bottom-right-radius:56px}
.banner{height:150px;border-bottom-right-radius:48px;text-align:center}
.banner-photo{position:absolute;inset:0;background:radial-gradient(ellipse at 30% 40%,var(--photo-light),transparent 60%),linear-gradient(100deg,var(--photo-mid),var(--photo-deep))}
.banner-photo::after{content:"";position:absolute;inset:0;background:rgba(20,26,14,.45)}
.banner-title{position:relative;padding-top:60px;font-size:26px;font-weight:500}
.banner-text{position:relative;font-size:6px;width:300px;margin:7px auto 0;opacity:.8;line-height:1.5}
.side-tab{position:absolute;right:0;top:110px;background:#fff;color:var(--ink);font-size:5px;padding:3px 6px;border-radius:2px 0 0 2px;z-index:2}
.hero .side-tab{top:68px}
.hero-copy{position:absolute;left:318px;top:100px;width:230px}
.hero-copy h1{font-size:24px;font-weight:700;line-height:1.2}
.hero-copy p{font-size:6px;line-height:1.5;margin-top:8px;opacity:.85}
.hero-phone{display:flex;align-items:center;gap:5px;font-size:7px;margin-top:10px}
.hero-phone i{width:10px;height:10px;border-radius:50%;background:var(--leaf);display:block}

/* services list */
.features{position:relative}
.features-photo{position:absolute;left:120px;top:26px;width:155px;height:155px;border-radius:4px;background:linear-gradient(160deg,#8d7460,#5b4434 60%,#3a2c22)}
.features-photo--blossom{background:linear-gradient(180deg,#a9c4dd 0,#d98aa3 35%,#b76b83 55%,#5f8a3a 80%)}
.features-tag{position:absolute;left:112px;top:150px;width:74px;background:var(--leaf);color:#fff;font-size:5.5px;line-height:1.4;padding:5px 7px}
.features-list{position:absolute;left:305px;top:30px;width:240px;display:grid;grid-template-columns:1fr 1fr;gap:16px 14px}
.feat{display:grid;grid-template-columns:14px 1fr;column-gap:6px}
.feat-icon{grid-row:span 2;width:12px;height:12px;border-radius:50%;background:var(--leaf-soft);display:flex;align-items:center;justify-content:center}
.feat h4{font-size:7px;font-weight:700}
.feat p{margin-top:2px;font-size:5.3px;color:var(--mute);line-height:1.45}

/* section heads */
.section-head{text-align:center}
.section-head h2{font-size:18px;font-weight:500}
.section-head p{font-size:5.8px;color:var(--mute);margin:5px auto 0;width:300px;line-height:1.5}
.divider{width:22px;height:1px;background:var(--leaf);margin:7px auto 0}

/* why choose */
.why{padding-top:4px;box-sizing:border-box}
.why-grid{display:flex;justify-content:center;gap:16px;margin-top:18px}
.why-item{width:82px;text-align:center}
.why-icon{width:18px;height:18px;border-radius:50%;border:1px solid #dfe5d6;margin:0 auto 5px;display:flex;align-items:center;justify-content:center}
.why-item h4{font-size:6.5px;font-weight:500}
.why-item p{font-size:5px;color:var(--mute);margin-top:3px;line-height:1.45}

/* grey band */
.band{position:relative;background:linear-gradient(var(--paper) 0 var(--split),var(--mist) var(--split))}
.work-cards{display:flex;justify-content:center;gap:10px}
.work-card{position:relative;width:190px;height:111px;border-radius:5px;background:radial-gradient(ellipse at 60% 40%,#7d8f56,transparent 60%),linear-gradient(120deg,#4a5535,#232b19)}
.work-label{position:absolute;left:6px;bottom:-6px;background:var(--leaf);color:#fff;font-size:5px;padding:4px 8px;border-radius:2px}
.stats{display:flex;justify-content:center;gap:58px;text-align:center}
.stat b{display:block;font-size:15px;font-weight:500}
.stat span{font-size:5px;color:var(--mute)}
.reviews{display:grid;grid-template-columns:190px 190px;gap:10px;justify-content:center}
.review{background:#fff;padding:10px 14px 9px;text-align:center;border-radius:2px}
.avatar{width:22px;height:22px;border-radius:50%;margin:0 auto 6px;background:linear-gradient(135deg,#c59a7a,#6d4b36)}
.review p{font-size:5.3px;color:var(--mute);line-height:1.55}
.review h4{font-size:6px;font-weight:700;margin-top:6px}
.review span{font-size:4.8px;color:var(--mute)}

/* questions */
.qa{position:relative;height:252px}
.qa-photo{position:absolute;left:150px;top:28px;width:131px;height:170px;border-radius:3px;background:linear-gradient(180deg,#9fc46a,#5c8f2c 55%,#2f5a17)}
.qa-tag{position:absolute;left:142px;top:168px;width:60px;background:var(--leaf);color:#fff;font-size:5px;padding:5px 6px;line-height:1.4}
.qa-copy{position:absolute;left:305px;top:32px;width:200px}
.qa-copy h3{font-size:11px;font-weight:500}
.qa-list{margin-top:8px;font-size:5.5px}
.qa-list li{margin-top:6px;padding-left:7px;position:relative}
.qa-list li::before{content:"";position:absolute;left:0;top:2px;width:3px;height:3px;border-radius:50%;background:var(--leaf)}
.qa-list .open{color:var(--leaf);font-weight:700}
.qa-list .answer{color:var(--mute);font-weight:400;line-height:1.55;margin-top:3px;padding-left:0}
.qa-list .answer::before{display:none}

/* call to action */
.cta{position:relative;height:162px;background:linear-gradient(90deg,#dde1e2,#eceeee 55%,#f5f6f5)}
.cta-text{position:absolute;left:110px;top:40px;width:230px}
.cta-text h3{font-size:15px;font-weight:500;line-height:1.25}
.cta-text p{font-size:5.5px;color:var(--mute);margin-top:7px;line-height:1.5}
.btn{display:inline-block;background:var(--leaf);color:#fff;font-size:5.5px;padding:4px 10px;border-radius:8px;margin-top:9px}
.cta-fern{position:absolute;right:0;top:0;width:120px;height:100%;background:radial-gradient(ellipse at 65% 45%,#6f7f5a 0,#b7c0ad 35%,transparent 70%)}

/* footer */
.footer{position:relative;height:148px;background:var(--forest);color:#c9d0c0;font-size:5.3px;line-height:1.6}
.footer-grid{position:absolute;left:110px;top:26px;display:grid;grid-template-columns:120px 90px 80px 100px;gap:12px}
.footer h4{color:#fff;font-size:7px;font-weight:500;margin-bottom:5px}
.footer .brand-mark{margin-bottom:6px}
.socials{display:flex;gap:4px;margin-top:6px}
.socials i{width:8px;height:8px;background:var(--leaf);display:block}
.footer-bar{position:absolute;left:110px;right:110px;bottom:12px;display:flex;justify-content:space-between;border-top:1px solid var(--forest-line);padding-top:6px;font-size:4.8px}

/* about */
.intro{position:relative;height:430px}
.mvv{display:flex;justify-content:center;gap:40px;padding-top:28px}
.mvv-item{width:100px;text-align:center}
.mvv-item h4{font-size:7px;font-weight:500}
.mvv-item p{font-size:5px;color:var(--mute);margin-top:3px;line-height:1.45}
.intro-photo{position:absolute;left:120px;top:118px;width:357px;height:200px;border-radius:4px;background:radial-gradient(ellipse at 50% 55%,#3f7d2a,#1f4a16 70%)}
.intro-copy{position:absolute;left:120px;top:340px;right:123px;display:flex;gap:22px}
.intro-copy h3{width:150px;font-size:10px;font-weight:500;line-height:1.3}
.intro-copy p{flex:1;font-size:5.3px;color:var(--mute);line-height:1.55}
.intro-rule{position:absolute;left:120px;right:123px;top:405px;height:1px;background:#e3e5e0}

/* gallery */
.gallery{position:relative;height:283px}
.gallery-grid{position:absolute;left:123px;top:38px;display:grid;grid-template-columns:repeat(3,115px);gap:5px}
.gallery-grid div{height:100px;border-radius:2px}

/* contact */
.contact{position:relative;height:271px}
.contact-head{position:absolute;left:110px;top:36px;right:105px;display:flex;gap:20px}
.contact-head h3{width:160px;font-size:11px;font-weight:500;white-space:nowrap}
.contact-head p{flex:1;font-size:5.3px;color:var(--mute);line-height:1.55}
.contact .socials{position:absolute;left:110px;top:70px}
.contact-details{position:absolute;left:120px;top:120px;width:120px}
.contact-details h4,.contact-form h4{font-size:7.5px;font-weight:500;margin-bottom:8px}
.detail{display:flex;gap:6px;margin-bottom:10px;font-size:5px;color:var(--mute);line-height:1.5}
.detail b{display:block;color:var(--ink);font-weight:500;font-size:5.5px}
.contact-form{position:absolute;left:268px;top:120px;width:160px}
.field{height:11px;border-bottom:1px solid #e1e3de;font-size:4.8px;color:#a6aaa2;margin-bottom:4px;line-height:11px}
.field--message{height:20px}
</style>
</head>
<body>

<!-- Home -->
<section class="page page--home" aria-label="Home page">
  <header class="hero">
    <div class="banner-photo" role="img" aria-label="Gardener tending potted plants in a greenhouse"></div>
    <nav class="nav"><span class="brand"><i class="brand-mark"></i>Quillby Tree Care</span><ul class="nav-links"><li>Home</li><li>About</li><li>Services</li><li>Gallery</li><li>Contact</li></ul><span class="nav-cta">Get a Quote</span></nav>
    <span class="side-tab">Quick Contact</span>
    <div class="hero-copy">
      <h1>Let's Beautify Your Garden Together!</h1>
      <p>Expert pruning, removal and tree health care for homes and parks across the county.</p>
      <div class="hero-phone"><i></i>Call Us: (555) 014-2290</div>
    </div>
  </header>
  <section class="features" style="height:240px">
    <div class="features-photo features-photo--blossom" role="img" aria-label="Blossoming tree on a green lawn"></div>
    <div class="features-tag">Trusted Tree Care For 10 Years</div>
    <div class="features-list">
      <div class="feat"><span class="feat-icon"><svg width="6" height="6" viewBox="0 0 6 6"><path d="M1 3l1.4 1.4L5 1.6" fill="none" stroke="#6f9b2c" stroke-width="1"/></svg></span><h4>Tree Pruning</h4><p>Careful cuts for healthy, safe growth.</p></div>
      <div class="feat"><span class="feat-icon"><svg width="6" height="6" viewBox="0 0 6 6"><path d="M1 3l1.4 1.4L5 1.6" fill="none" stroke="#6f9b2c" stroke-width="1"/></svg></span><h4>Tree Removal</h4><p>Safe removal of dead or risky trees.</p></div>
      <div class="feat"><span class="feat-icon"><svg width="6" height="6" viewBox="0 0 6 6"><path d="M1 3l1.4 1.4L5 1.6" fill="none" stroke="#6f9b2c" stroke-width="1"/></svg></span><h4>Stump Grinding</h4><p>Clear stumps right below the soil.</p></div>
      <div class="feat"><span class="feat-icon"><svg width="6" height="6" viewBox="0 0 6 6"><path d="M1 3l1.4 1.4L5 1.6" fill="none" stroke="#6f9b2c" stroke-width="1"/></svg></span><h4>Preservation</h4><p>Feeding and care for mature trees.</p></div>
      <div class="feat"><span class="feat-icon"><svg width="6" height="6" viewBox="0 0 6 6"><path d="M1 3l1.4 1.4L5 1.6" fill="none" stroke="#6f9b2c" stroke-width="1"/></svg></span><h4>Cabling</h4><p>Support for weak limbs and trunks.</p></div>
      <div class="feat"><span class="feat-icon"><svg width="6" height="6" viewBox="0 0 6 6"><path d="M1 3l1.4 1.4L5 1.6" fill="none" stroke="#6f9b2c" stroke-width="1"/></svg></span><h4>Emergency</h4><p>Storm response any time of day.</p></div>
    </div>
  </section>
  <section class="why" style="height:175px">
    <div class="section-head"><h2>Why Choose Us</h2><p>Certified arborists who treat every yard like their own.</p><div class="divider"></div></div>
    <div class="why-grid">
      <div class="why-item"><div class="why-icon"><svg width="8" height="8" viewBox="0 0 8 8"><circle cx="4" cy="4" r="2.5" fill="none" stroke="#6f9b2c"/></svg></div><h4>Certified Team</h4><p>Trained and insured crew.</p></div>
      <div class="why-item"><div class="why-icon"><svg width="8" height="8" viewBox="0 0 8 8"><circle cx="4" cy="4" r="2.5" fill="none" stroke="#6f9b2c"/></svg></div><h4>Fair Pricing</h4><p>Clear quotes, no surprises.</p></div>
      <div class="why-item"><div class="why-icon"><svg width="8" height="8" viewBox="0 0 8 8"><circle cx="4" cy="4" r="2.5" fill="none" stroke="#6f9b2c"/></svg></div><h4>Fast Response</h4><p>Crews out the same day.</p></div>
      <div class="why-item"><div class="why-icon"><svg width="8" height="8" viewBox="0 0 8 8"><circle cx="4" cy="4" r="2.5" fill="none" stroke="#6f9b2c"/></svg></div><h4>Clean Finish</h4><p>We leave every yard tidy.</p></div>
    </div>
  </section>
  <section class="band" style="--split:92px;height:582px">
    <div class="work-cards">
      <div class="work-card" role="img" aria-label="Arborist trimming a shrub"><span class="work-label">Tree Pruning</span></div>
      <div class="work-card" role="img" aria-label="Hands planting a young tree"><span class="work-label">Tree Planting</span></div>
    </div>
    <div class="stats" style="margin-top:30px">
      <div class="stat"><b>698</b><span>Happy Clients</span></div>
      <div class="stat"><b>1,106</b><span>Trees Pruned</span></div>
      <div class="stat"><b>4,469</b><span>Stumps Ground</span></div>
      <div class="stat"><b>754</b><span>Projects Done</span></div>
    </div>
    <div class="section-head" style="margin-top:34px"><h2>What Our Clients Say</h2><p>Kind words from homeowners we have helped.</p><div class="divider"></div></div>
    <div class="reviews" style="margin-top:16px">
      <div class="review"><div class="avatar" role="img" aria-label="Client portrait"></div><p>The crew removed two old oaks and left the lawn spotless. Friendly, fast and careful the whole way.</p><h4>Mara Lindell</h4><span>Homeowner</span></div>
      <div class="review"><div class="avatar" role="img" aria-label="Client portrait"></div><p>They came out the night of the storm and cleared the drive. Honest price and great work.</p><h4>Tom Brevik</h4><span>Homeowner</span></div>
      <div class="review"><div class="avatar" role="img" aria-label="Client portrait"></div><p>Our maples look healthier than ever after their pruning. We will book them every year now.</p><h4>Nina Calder</h4><span>Property Manager</span></div>
      <div class="review"><div class="avatar" role="img" aria-label="Client portrait"></div><p>Stump grinding was done in an hour and the yard was raked clean after. Highly recommend.</p><h4>Owen Pratt</h4><span>Homeowner</span></div>
    </div>
  </section>
  <section class="qa">
    <div class="qa-photo" role="img" aria-label="Watering can on a sunny lawn"></div>
    <div class="qa-tag">Caring For Trees Since 2014</div>
    <div class="qa-copy">
      <h3>Questions &amp; Answers</h3>
      <ul class="qa-list">
        <li class="open">How often should trees be pruned?</li>
        <li class="answer">Most trees do best with a light prune every two to three years, timed to the season and species.</li>
        <li>Do you offer free quotes?</li>
        <li>Are you licensed and insured?</li>
      </ul>
    </div>
  </section>
  <section class="cta">
    <div class="cta-text"><h3>Let's Bring Nature Into Your Lovely House</h3><p>Book a visit and our arborists will plan the right care for your trees.</p><span class="btn">Get a Quote</span></div>
    <div class="cta-fern" role="img" aria-label="Fern fronds"></div>
  </section>
  <footer class="footer">
    <div class="footer-grid">
      <div><i class="brand-mark"></i><p>Full service tree care for homes, parks and businesses in the county.</p></div>
      <div><h4>Contact Info</h4><p>48 Fernway Road, Ashford</p><p>(555) 014-2290</p><p>hello@quillbytree.com</p></div>
      <div><h4>Service</h4><p>Tree Pruning</p><p>Tree Removal</p><p>Stump Grinding</p><p>Emergency Care</p></div>
      <div><h4>Get In Touch</h4><p>Follow our latest projects and seasonal tips.</p><div class="socials"><i></i><i></i><i></i></div></div>
    </div>
    <div class="footer-bar"><span>© 2024 Quillby Tree Care</span><span>All rights reserved</span></div>
  </footer>
</section>

<!-- Services -->
<section class="page page--services" aria-label="Services page">
  <header class="banner">
    <div class="banner-photo" role="img" aria-label="Orange flowers among dark foliage"></div>
    <nav class="nav"><span class="brand"><i class="brand-mark"></i>Quillby Tree Care</span><ul class="nav-links"><li>Home</li><li>About</li><li>Services</li><li>Gallery</li><li>Contact</li></ul><span class="nav-cta">Get a Quote</span></nav>
    <span class="side-tab">Quick Contact</span>
    <h1 class="banner-title">Services</h1>
    <p class="banner-text">From routine pruning to storm clean up, our crew handles every tree need with care.</p>
  </header>
  <section class="features" style="height:265px">
    <div class="features-photo" role="img" aria-label="Garden tools in fresh soil"></div>
    <div class="features-tag">Let's Bring Your Garden Back To Life</div>
    <div class="features-list">
      <div class="feat"><span class="feat-icon"><svg width="6" height="6" viewBox="0 0 6 6"><path d="M1 3l1.4 1.4L5 1.6" fill="none" stroke="#6f9b2c" stroke-width="1"/></svg></span><h4>Tree Pruning</h4><p>Careful cuts for healthy, safe growth.</p></div>
      <div class="feat"><span class="feat-icon"><svg width="6" height="6" viewBox="0 0 6 6"><path d="M1 3l1.4 1.4L5 1.6" fill="none" stroke="#6f9b2c" stroke-width="1"/></svg></span><h4>Tree Removal</h4><p>Safe removal of dead or risky trees.</p></div>
      <div class="feat"><span class="feat-icon"><svg width="6" height="6" viewBox="0 0 6 6"><path d="M1 3l1.4 1.4L5 1.6" fill="none" stroke="#6f9b2c" stroke-width="1"/></svg></span><h4>Stump Grinding</h4><p>Clear stumps right below the soil.</p></div>
      <div class="feat"><span class="feat-icon"><svg width="6" height="6" viewBox="0 0 6 6"><path d="M1 3l1.4 1.4L5 1.6" fill="none" stroke="#6f9b2c" stroke-width="1"/></svg></span><h4>Preservation</h4><p>Feeding and care for mature trees.</p></div>
      <div class="feat"><span class="feat-icon"><svg width="6" height="6" viewBox="0 0 6 6"><path d="M1 3l1.4 1.4L5 1.6" fill="none" stroke="#6f9b2c" stroke-width="1"/></svg></span><h4>Cabling</h4><p>Support for weak limbs and trunks.</p></div>
      <div class="feat"><span class="feat-icon"><svg width="6" height="6" viewBox="0 0 6 6"><path d="M1 3l1.4 1.4L5 1.6" fill="none" stroke="#6f9b2c" stroke-width="1"/></svg></span><h4>Emergency</h4><p>Storm response any time of day.</p></div>
    </div>
  </section>
  <section class="band" style="--split:0px;height:440px">
    <div class="stats" style="padding-top:30px">
      <div class="stat"><b>698</b><span>Happy Clients</span></div>
      <div class="stat"><b>1,106</b><span>Trees Pruned</span></div>
      <div class="stat"><b>4,469</b><span>Stumps Ground</span></div>
      <div class="stat"><b>754</b><span>Projects Done</span></div>
    </div>
    <div class="section-head" style="margin-top:42px"><h2>What Our Clients Say</h2><p>Kind words from homeowners we have helped.</p><div class="divider"></div></div>
    <div class="reviews" style="margin-top:22px;gap:14px 10px">
      <div class="review"><div class="avatar" role="img" aria-label="Client portrait"></div><p>The crew removed two old oaks and left the lawn spotless. Friendly, fast and careful the whole way.</p><h4>Mara Lindell</h4><span>Homeowner</span></div>
      <div class="review"><div class="avatar" role="img" aria-label="Client portrait"></div><p>They came out the night of the storm and cleared the drive. Honest price and great work.</p><h4>Tom Brevik</h4><span>Homeowner</span></div>
      <div class="review"><div class="avatar" role="img" aria-label="Client portrait"></div><p>Our maples look healthier than ever after their pruning. We will book them every year now.</p><h4>Nina Calder</h4><span>Property Manager</span></div>
      <div class="review"><div class="avatar" role="img" aria-label="Client portrait"></div><p>Stump grinding was done in an hour and the yard was raked clean after. Highly recommend.</p><h4>Owen Pratt</h4><span>Homeowner</span></div>
    </div>
  </section>
  <section class="cta">
    <div class="cta-text"><h3>Let's Bring Nature Into Your Lovely House</h3><p>Book a visit and our arborists will plan the right care for your trees.</p><span class="btn">Get a Quote</span></div>
    <div class="cta-fern" role="img" aria-label="Fern fronds"></div>
  </section>
  <footer class="footer" style="height:147px">
    <div class="footer-grid">
      <div><i class="brand-mark"></i><p>Full service tree care for homes, parks and businesses in the county.</p></div>
      <div><h4>Contact Info</h4><p>48 Fernway Road, Ashford</p><p>(555) 014-2290</p><p>hello@quillbytree.com</p></div>
      <div><h4>Service</h4><p>Tree Pruning</p><p>Tree Removal</p><p>Stump Grinding</p><p>Emergency Care</p></div>
      <div><h4>Get In Touch</h4><p>Follow our latest projects and seasonal tips.</p><div class="socials"><i></i><i></i><i></i></div></div>
    </div>
    <div class="footer-bar"><span>© 2024 Quillby Tree Care</span><span>All rights reserved</span></div>
  </footer>
</section>

<!-- About -->
<section class="page page--about" aria-label="About page">
  <header class="banner" style="height:160px">
    <div class="banner-photo" role="img" aria-label="Soft focus green foliage"></div>
    <nav class="nav"><span class="brand"><i class="brand-mark"></i>Quillby Tree Care</span><ul class="nav-links"><li>Home</li><li>About</li><li>Services</li><li>Gallery</li><li>Contact</li></ul><span class="nav-cta">Get a Quote</span></nav>
    <span class="side-tab">Quick Contact</span>
    <h1 class="banner-title">About</h1>
    <p class="banner-text">A local family team caring for trees, yards and neighbourhoods for over ten years.</p>
  </header>
  <section class="intro">
    <div class="mvv">
      <div class="mvv-item"><div class="why-icon"><svg width="8" height="8" viewBox="0 0 8 8"><circle cx="4" cy="4" r="2.5" fill="none" stroke="#6f9b2c"/></svg></div><h4>Mission</h4><p>Keep every tree healthy and every yard safe.</p></div>
      <div class="mvv-item"><div class="why-icon"><svg width="8" height="8" viewBox="0 0 8 8"><circle cx="4" cy="4" r="2.5" fill="none" stroke="#6f9b2c"/></svg></div><h4>Vision</h4><p>Greener streets for the next generation.</p></div>
      <div class="mvv-item"><div class="why-icon"><svg width="8" height="8" viewBox="0 0 8 8"><circle cx="4" cy="4" r="2.5" fill="none" stroke="#6f9b2c"/></svg></div><h4>Values</h4><p>Safety, honesty and respect for nature.</p></div>
    </div>
    <div class="intro-photo" role="img" aria-label="Person holding large green leaves"></div>
    <div class="intro-copy">
      <h3>We Provide The Best Tree Care For 10 Years</h3>
      <p>Our certified arborists prune, remove and protect trees of every size. We plan each job with care, use modern gear and always leave your property clean and safe.</p>
    </div>
    <div class="intro-rule"></div>
  </section>
  <section class="why" style="height:177px;padding-top:18px">
    <div class="section-head"><h2>Why Choose Us</h2><p>Certified arborists who treat every yard like their own.</p><div class="divider"></div></div>
    <div class="why-grid">
      <div class="why-item"><div class="why-icon"><svg width="8" height="8" viewBox="0 0 8 8"><circle cx="4" cy="4" r="2.5" fill="none" stroke="#6f9b2c"/></svg></div><h4>Certified Team</h4><p>Trained and insured crew.</p></div>
      <div class="why-item"><div class="why-icon"><svg width="8" height="8" viewBox="0 0 8 8"><circle cx="4" cy="4" r="2.5" fill="none" stroke="#6f9b2c"/></svg></div><h4>Fair Pricing</h4><p>Clear quotes, no surprises.</p></div>
      <div class="why-item"><div class="why-icon"><svg width="8" height="8" viewBox="0 0 8 8"><circle cx="4" cy="4" r="2.5" fill="none" stroke="#6f9b2c"/></svg></div><h4>Fast Response</h4><p>Crews out the same day.</p></div>
      <div class="why-item"><div class="why-icon"><svg width="8" height="8" viewBox="0 0 8 8"><circle cx="4" cy="4" r="2.5" fill="none" stroke="#6f9b2c"/></svg></div><h4>Clean Finish</h4><p>We leave every yard tidy.</p></div>
    </div>
  </section>
  <section class="band" style="--split:83px;height:217px">
    <div class="work-cards">
      <div class="work-card" role="img" aria-label="Arborist trimming a shrub"><span class="work-label">Tree Pruning</span></div>
      <div class="work-card" role="img" aria-label="Hands planting a young tree"><span class="work-label">Tree Planting</span></div>
    </div>
    <div class="stats" style="margin-top:16px">
      <div class="stat"><b>698</b><span>Happy Clients</span></div>
      <div class="stat"><b>1,106</b><span>Trees Pruned</span></div>
      <div class="stat"><b>4,469</b><span>Stumps Ground</span></div>
      <div class="stat"><b>754</b><span>Projects Done</span></div>
    </div>
  </section>
  <section class="cta" style="height:151px">
    <div class="cta-text" style="top:36px"><h3>Let's Bring Nature Into Your Lovely House</h3><p>Book a visit and our arborists will plan the right care for your trees.</p><span class="btn">Get a Quote</span></div>
    <div class="cta-fern" role="img" aria-label="Fern fronds"></div>
  </section>
  <footer class="footer" style="height:133px">
    <div class="footer-grid">
      <div><i class="brand-mark"></i><p>Full service tree care for homes, parks and businesses in the county.</p></div>
      <div><h4>Contact Info</h4><p>48 Fernway Road, Ashford</p><p>(555) 014-2290</p><p>hello@quillbytree.com</p></div>
      <div><h4>Service</h4><p>Tree Pruning</p><p>Tree Removal</p><p>Stump Grinding</p><p>Emergency Care</p></div>
      <div><h4>Get In Touch</h4><p>Follow our latest projects and seasonal tips.</p><div class="socials"><i></i><i></i><i></i></div></div>
    </div>
    <div class="footer-bar"><span>© 2024 Quillby Tree Care</span><span>All rights reserved</span></div>
  </footer>
</section>

<!-- Gallery -->
<section class="page page--gallery" aria-label="Gallery page">
  <header class="banner" style="height:142px">
    <div class="banner-photo" role="img" aria-label="Dark green leaves and blossoms"></div>
    <nav class="nav"><span class="brand"><i class="brand-mark"></i>Quillby Tree Care</span><ul class="nav-links"><li>Home</li><li>About</li><li>Services</li><li>Gallery</li><li>Contact</li></ul><span class="nav-cta">Get a Quote</span></nav>
    <span class="side-tab">Quick Contact</span>
    <h1 class="banner-title" style="padding-top:50px">Gallery</h1>
    <p class="banner-text">A look at recent pruning, removal and landscape projects from our crew.</p>
  </header>
  <section class="gallery">
    <div class="gallery-grid">
      <div role="img" aria-label="Seedling growing from soil" style="background:linear-gradient(160deg,#6b8a3a,#2e2a1c)"></div>
      <div role="img" aria-label="Garden path across a lawn" style="background:linear-gradient(180deg,#8fb0c4,#5f8a34 45%,#3d6a22)"></div>
      <div role="img" aria-label="White daisy flowers" style="background:radial-gradient(circle at 50% 50%,#f2f0e6,#c9c7a8 40%,#44602a 75%)"></div>
      <div role="img" aria-label="Young green sprout" style="background:radial-gradient(circle at 50% 60%,#a8cf56,#2d3a1e 70%)"></div>
      <div role="img" aria-label="Ride-on mower on grass" style="background:linear-gradient(180deg,#9cbbe0,#5a6f8a 45%,#4f7f2c 70%)"></div>
      <div role="img" aria-label="Formal garden with fountain" style="background:linear-gradient(180deg,#a7b8a6,#6a8b4e 50%,#3e5a2a)"></div>
    </div>
  </section>
  <section class="cta" style="height:161px">
    <div class="cta-text"><h3>Let's Bring Nature Into Your Lovely House</h3><p>Book a visit and our arborists will plan the right care for your trees.</p><span class="btn">Get a Quote</span></div>
    <div class="cta-fern" role="img" aria-label="Fern fronds"></div>
  </section>
  <footer class="footer">
    <div class="footer-grid">
      <div><i class="brand-mark"></i><p>Full service tree care for homes, parks and businesses in the county.</p></div>
      <div><h4>Contact Info</h4><p>48 Fernway Road, Ashford</p><p>(555) 014-2290</p><p>hello@quillbytree.com</p></div>
      <div><h4>Service</h4><p>Tree Pruning</p><p>Tree Removal</p><p>Stump Grinding</p><p>Emergency Care</p></div>
      <div><h4>Get In Touch</h4><p>Follow our latest projects and seasonal tips.</p><div class="socials"><i></i><i></i><i></i></div></div>
    </div>
    <div class="footer-bar"><span>© 2024 Quillby Tree Care</span><span>All rights reserved</span></div>
  </footer>
</section>

<!-- Contact -->
<section class="page page--contact" aria-label="Contact page">
  <header class="banner" style="height:138px">
    <div class="banner-photo" role="img" aria-label="Purple flowers over dark foliage"></div>
    <nav class="nav"><span class="brand"><i class="brand-mark"></i>Quillby Tree Care</span><ul class="nav-links"><li>Home</li><li>About</li><li>Services</li><li>Gallery</li><li>Contact</li></ul><span class="nav-cta">Get a Quote</span></nav>
    <h1 class="banner-title" style="padding-top:52px">Contact</h1>
    <p class="banner-text">Tell us about your trees and we will reply within one business day.</p>
  </header>
  <section class="contact">
    <div class="contact-head">
      <h3>Getting in Touch is Easy!</h3>
      <p>Call, email or send the form below. Our team will set up a visit and give you a clear quote for the work.</p>
    </div>
    <div class="socials"><i></i><i></i><i></i></div>
    <div class="contact-details">
      <h4>Contact Details</h4>
      <div class="detail"><svg width="7" height="9" viewBox="0 0 7 9"><path d="M3.5 8.5C1.5 6 .5 4.5.5 3.3a3 3 0 016 0C6.5 4.5 5.5 6 3.5 8.5z" fill="#6f9b2c"/></svg><div><b>Address</b>48 Fernway Road, Ashford</div></div>
      <div class="detail"><svg width="7" height="9" viewBox="0 0 7 9"><path d="M3.5 8.5C1.5 6 .5 4.5.5 3.3a3 3 0 016 0C6.5 4.5 5.5 6 3.5 8.5z" fill="#6f9b2c"/></svg><div><b>Phone</b>(555) 014-2290</div></div>
      <div class="detail"><svg width="7" height="9" viewBox="0 0 7 9"><path d="M3.5 8.5C1.5 6 .5 4.5.5 3.3a3 3 0 016 0C6.5 4.5 5.5 6 3.5 8.5z" fill="#6f9b2c"/></svg><div><b>Email</b>hello@quillbytree.com</div></div>
    </div>
    <div class="contact-form">
      <h4>Send Us a Message</h4>
      <div class="field">Your Name</div>
      <div class="field">Email Address</div>
      <div class="field">Phone</div>
      <div class="field field--message">Message</div>
      <span class="btn">Send</span>
    </div>
  </section>
  <div style="height:202px"></div>
  <footer class="footer">
    <div class="footer-grid">
      <div><i class="brand-mark"></i><p>Full service tree care for homes, parks and businesses in the county.</p></div>
      <div><h4>Contact Info</h4><p>48 Fernway Road, Ashford</p><p>(555) 014-2290</p><p>hello@quillbytree.com</p></div>
      <div><h4>Service</h4><p>Tree Pruning</p><p>Tree Removal</p><p>Stump Grinding</p><p>Emergency Care</p></div>
      <div><h4>Get In Touch</h4><p>Follow our latest projects and seasonal tips.</p><div class="socials"><i></i><i></i><i></i></div></div>
    </div>
    <div class="footer-bar"><span>© 2024 Quillby Tree Care</span><span>All rights reserved</span></div>
  </footer>
</section>

</body>
</html>
```